Postcard bar mitzvah invitations

I'm looking for glossy postcards which which contain information for my son's bar mitzvah - the time and place of the service, that it will be followed by a luncheon, the time and place of the party, and how to RSVP.

```html
<!DOCTYPE html>
<html lang="en">
<head>
<meta charset="utf-8">
<title>Bar Mitzvah Invitation and RSVP Postcard</title>
<link rel="stylesheet" href="https://fonts.googleapis.com/css2?family=Cabin:wght@400;500&family=Great+Vibes&family=Marcellus&display=swap">
<style>
  :root {
    --backdrop: #e6e6e4;
    --paper: #ffffff;
    --mint: #bfe3d6;
    --mint-soft: #cde9df;
    --brown: #8e6b51;
    --teal: #1f9488;
    --ribbon: #5fbfa6;
    --ink: #1e1e1e;
    --rule-dark: #4a4a4a;
    --rule-light: #c9c9c9;
  }
  * { box-sizing: border-box; margin: 0; padding: 0; }
  html, body { width: 1200px; height: 724px; overflow: hidden; }
  body {
    position: relative;
    background: var(--backdrop);
    font-family: "Cabin", "Trebuchet MS", sans-serif;
    color: var(--ink);
  }
  .card {
    position: absolute;
    background: var(--paper);
    overflow: hidden;
    box-shadow: 0 3px 10px rgba(0,0,0,0.25);
  }
  .invite { left: 45px; top: 43px; width: 462px; height: 595px; }
  .reply  { left: 549px; top: 176px; width: 598px; height: 462px; }

  .top-band { position: absolute; left: 0; top: 0; width: 100%; height: 30px; background: var(--mint); }
  .top-rule { position: absolute; left: 0; top: 30px; width: 100%; height: 7px; background: var(--brown); }
  .pattern-band {
    position: absolute; left: 0; width: 100%; height: 15px;
    background: linear-gradient(90deg, var(--teal), var(--brown) 30%, var(--mint) 55%, var(--teal) 78%, var(--brown));
    opacity: 0.8;
  }
  .bottom-band { position: absolute; left: 0; bottom: 0; width: 100%; background: var(--mint); }

  .emblem { position: absolute; display: block; }
  .line { position: absolute; left: 0; width: 100%; text-align: center; white-space: nowrap; }

  .invite .emblem { left: 199px; top: 9px; }
  .invite .pattern-band { top: 540px; }
  .invite .bottom-band { height: 37px; }

  .lead { font-family: "Marcellus", serif; font-size: 16px; top: 96px; }
  .honoree { font-family: "Great Vibes", cursive; font-size: 40px; color: var(--teal); top: 120px; }
  .ribbon { position: absolute; left: 22px; top: 171px; }
  .ribbon-text { font-size: 15px; color: #fff; top: 176px; }
  .date { font-size: 19px; color: var(--teal); top: 209px; }
  .venue { font-size: 16.5px; top: 252px; }
  .venue-address { font-size: 17px; top: 274px; }
  .dotted { position: absolute; left: 22px; width: 418px; border-top: 2px dotted #555; }
  .parents { font-size: 16.5px; color: var(--teal); top: 312px; }
  .rsvp-line { font-size: 13px; top: 345px; }
  .ornament-row { position: absolute; left: 0; top: 376px; width: 100%; height: 48px; }
  .sprig { position: absolute; top: 14px; width: 76px; height: 20px; border-radius: 10px;
           background: linear-gradient(90deg, rgba(139,139,139,0.15), rgba(139,139,139,0.55), rgba(139,139,139,0.15)); }
  .invite .sprig.left { left: 106px; }
  .invite .sprig.right { left: 280px; }
  .invite .ornament-row .emblem { left: 207px; top: 0; }
  .lunch { font-size: 17px; color: var(--teal); top: 435px; }
  .heavy-rule { position: absolute; left: 22px; top: 460px; width: 418px; height: 3px; background: var(--rule-dark); }
  .party-time { font-size: 16.5px; top: 469px; }
  .party-place { font-size: 16.5px; top: 488px; }
  .party-address { font-size: 16.5px; top: 507px; }

  .reply .emblem { left: 130px; top: 19px; }
  .reply .pattern-band { top: 409px; }
  .reply .bottom-band { height: 35px; }
  .stamp-box { position: absolute; left: 495px; top: 59px; width: 81px; height: 61px; border: 1px solid #bdbdbd; }
  .address-rule { position: absolute; left: 362px; width: 208px; height: 1px; background: var(--rule-light); }
  .reply-title { position: absolute; left: 23px; top: 90px; font-size: 29px; font-weight: 400; color: var(--teal); }
  .reply-detail { position: absolute; left: 23px; font-size: 16px; }
  .reply .center { left: 32px; width: 268px; }
  .reply .date { font-size: 14.5px; top: 218px; }
  .reply .ornament-row { left: 32px; top: 244px; width: 268px; height: 30px; }
  .reply .sprig { top: 8px; width: 54px; height: 14px; border-radius: 7px; }
  .reply .sprig.left { left: 46px; }
  .reply .sprig.right { left: 168px; }
  .reply .ornament-row .emblem { left: 121px; top: 0; }
  .small { font-size: 11.5px; }
  .reply .venue { top: 278px; }
  .reply .venue-address { top: 292px; }
  .divider { position: absolute; left: 32px; top: 312px; width: 268px; height: 1px; background: #777; }
  .divider::after { content: ""; position: absolute; left: 131px; top: -2px; width: 5px; height: 5px; border-radius: 50%; background: #555; }
  .reply .lunch { font-size: 13px; top: 322px; }
  .reply .party-time { top: 340px; }
  .reply .party-place { top: 355px; }
  .reply .party-address { top: 369px; }
</style>
</head>
<body>

<section class="card invite" aria-label="Bar mitzvah invitation">
  <div class="top-band"></div>
  <div class="top-rule"></div>
  <svg class="emblem" width="64" height="64" viewBox="0 0 64 64" aria-hidden="true">
    <circle cx="32" cy="32" r="32" fill="#1f9488"/>
    <polygon points="32,14 47.6,41 16.4,41" fill="none" stroke="#fff" stroke-width="2.6"/>
    <polygon points="32,50 16.4,23 47.6,23" fill="none" stroke="#fff" stroke-width="2.6"/>
  </svg>

  <p class="line lead">Please Join Us As We Celebrate</p>
  <p class="line honoree">Ethan Marlow</p>
  <svg class="ribbon" width="418" height="28" viewBox="0 0 418 28" aria-hidden="true">
    <polygon points="0,0 418,0 408,14 418,28 0,28 10,14" fill="#5fbfa6"/>
    <circle cx="25" cy="14" r="2.5" fill="#fff"/>
    <circle cx="393" cy="14" r="2.5" fill="#fff"/>
  </svg>
  <p class="line ribbon-text">as he called to the Torah as a Bar Mitzvah</p>
  <p class="line date">June 13th, 2015 10:30 am</p>
  <p class="line venue">Temple Beth Elior</p>
  <p class="line venue-address">4410 Cedarbrook Road, Maple Hollow, Ohio 44000</p>
  <div class="dotted" style="top:307px"></div>
  <p class="line parents">Parents: Laura and Mark Marlow</p>
  <div class="dotted" style="top:335px"></div>
  <p class="line rsvp-line">RSVP by May 31st - marlowfam18@mailbox.com -or- 216-555-0143</p>

  <div class="ornament-row">
    <div class="sprig left" role="img" aria-label="Leafy branch ornament"></div>
    <svg class="emblem" width="48" height="48" viewBox="0 0 64 64" aria-hidden="true">
      <circle cx="32" cy="32" r="32" fill="#bfe3d6"/>
      <polygon points="32,14 47.6,41 16.4,41" fill="none" stroke="#fff" stroke-width="3"/>
      <polygon points="32,50 16.4,23 47.6,23" fill="none" stroke="#fff" stroke-width="3"/>
    </svg>
    <div class="sprig right" role="img" aria-label="Leafy branch ornament"></div>
  </div>

  <p class="line lunch">Light lunch following&nbsp; Bar Mitzvah</p>
  <div class="heavy-rule"></div>
  <p class="line party-time">4:00 pm to 8:00 pm</p>
  <p class="line party-place">Celebration continues at Jump 'n' Play</p>
  <p class="line party-address">782 Ridgeview Road, Pine Crest, Ohio 44000</p>

  <div class="pattern-band" role="img" aria-label="Decorative border pattern in teal, mint and brown"></div>
  <div class="bottom-band"></div>
</section>

<section class="card reply" aria-label="RSVP postcard">
  <div class="top-band"></div>
  <div class="top-rule"></div>
  <svg class="emblem" width="64" height="64" viewBox="0 0 64 64" aria-hidden="true">
    <circle cx="32" cy="32" r="32" fill="#1f9488"/>
    <polygon points="32,14 47.6,41 16.4,41" fill="none" stroke="#fff" stroke-width="2.6"/>
    <polygon points="32,50 16.4,23 47.6,23" fill="none" stroke="#fff" stroke-width="2.6"/>
  </svg>

  <div class="stamp-box"></div>
  <div class="address-rule" style="top:159px"></div>
  <div class="address-rule" style="top:194px"></div>
  <div class="address-rule" style="top:228px"></div>
  <div class="address-rule" style="top:263px"></div>

  <h1 class="reply-title">RSVP</h1>
  <p class="reply-detail" style="top:132px">by May 31st - marlowfam18@mailbox.com</p>
  <p class="reply-detail" style="top:153px">or - 216-555-0143</p>

  <p class="line center date">June 13th, 2015 10:30 am</p>
  <div class="ornament-row">
    <div class="sprig left" role="img" aria-label="Leafy branch ornament"></div>
    <svg class="emblem" width="30" height="30" viewBox="0 0 64 64" aria-hidden="true">
      <circle cx="32" cy="32" r="32" fill="#bfe3d6"/>
      <polygon points="32,14 47.6,41 16.4,41" fill="none" stroke="#fff" stroke-width="3.5"/>
      <polygon points="32,50 16.4,23 47.6,23" fill="none" stroke="#fff" stroke-width="3.5"/>
    </svg>
    <div class="sprig right" role="img" aria-label="Leafy branch ornament"></div>
  </div>
  <p class="line center small venue">Temple Beth Elior</p>
  <p class="line center small venue-address">4410 Cedarbrook Road, Maple Hollow, Ohio 44000</p>
  <div class="divider"></div>
  <p class="line center lunch">Light lunch following&nbsp; Bar Mitzvah</p>
  <p class="line center small party-time">4:00 pm to 8:00 pm</p>
  <p class="line center small party-place">Celebration continues at Jump 'n' Play</p>
  <p class="line center small party-address">782 Ridgeview Road, Pine Crest, Ohio 44000</p>

  <div class="pattern-band" role="img" aria-label="Decorative border pattern in teal, mint and brown"></div>
  <div class="bottom-band"></div>
</section>

</body>
</html>
```